Thank You Card

I'm looking for a thank you card design using our logo and other graphics. We are an essential business and our employees (Electricians) have done an incredible job staying healthy and safe during the COVID-19 pandemic, I want to send each a thank you card.

```html
<!DOCTYPE html>
<html lang="en">
<head>
<meta charset="utf-8">
<title>Thank You Card</title>
<link rel="stylesheet" href="https://fonts.googleapis.com/css2?family=Quicksand:wght@300;700&family=Dancing+Script:wght@400&display=swap">
<style>
  :root {
    --card-red: #ee4c57;
    --text-white: #ffffff;
    --shirt-blue: #3f9be0;
    --trouser-charcoal: #3b3a3c;
  }
  * { margin: 0; padding: 0; box-sizing: border-box; }
  html, body {
    width: 1200px;
    height: 852px;
    overflow: hidden;
    background: var(--card-red);
  }
  .card {
    position: relative;
    width: 1200px;
    height: 852px;
    background: var(--card-red);
    color: var(--text-white);
  }
  .electrician-illustration {
    position: absolute;
    left: 69px;
    top: 120px;
    width: 360px;
    height: 680px;
    border-radius: 12px;
    background: linear-gradient(180deg, var(--shirt-blue) 0%, var(--shirt-blue) 40%, var(--trouser-charcoal) 100%);
    opacity: 0.85;
  }
  .message {
    position: absolute;
    left: 560px;
    top: 176px;
    width: 474px;
    text-align: center;
    font-family: "Quicksand", sans-serif;
    font-weight: 300;
    font-size: 32px;
    line-height: 42px;
    letter-spacing: 1px;
  }
  .thank-you {
    position: absolute;
    left: 540px;
    top: 380px;
    width: 514px;
    height: 200px;
    text-align: center;
    white-space: nowrap;
    font-family: "Dancing Script", cursive;
    font-weight: 400;
    font-size: 150px;
    line-height: 150px;
  }
  .company-name {
    position: absolute;
    left: 600px;
    top: 664px;
    width: 394px;
    text-align: center;
    white-space: nowrap;
    font-family: "Quicksand", sans-serif;
    font-weight: 700;
    font-size: 32px;
    line-height: 40px;
    letter-spacing: 1px;
    text-transform: uppercase;
  }
</style>
</head>
<body>
  <main class="card">
    <div class="electrician-illustration" role="img" aria-label="Illustration of an electrician in a hard hat, face mask, blue shirt and gloves, holding a toolbox and screwdriver"></div>
    <p class="message">You have done an incredi-<br>ble job staying healthy and<br>safe during the COVID-19<br>pandemic</p>
    <h1 class="thank-you">thank you</h1>
    <p class="company-name">Brightline<br>Electric Services</p>
  </main>
</body>
</html>
```